Meadow Moe''s Funhouse Website Revamp

We have a children's entertainment center that hasn't changed in 20 years and the site looks like it was created 20 years ago. We need a new, modern, clean site that pops. Attached is the new logo that should be used as a style guide.

Current site is: www.meadowmoesfun.example

Thanks!
Updates

Designers, thank you all for the amazing work. It was exciting to be able to go through and see all the creativity that came in. I have decided on a design but wanted to share my thanks and appreciation for your time. Warm regards, Calvin

Target Market(s)

Mothers with children in the 2 - 14 range.

Industry/Entity Type

Entertainment

```html
<!DOCTYPE html>
<html lang="en">
<head>
<meta charset="utf-8">
<title>Meadow Moe's Funhouse – Parties</title>
<link href="https://fonts.googleapis.com/css2?family=Open+Sans:ital,wght@0,400;0,600;0,700;1,400;1,600&display=swap" rel="stylesheet">
<style>
:root{
  --sky:#7fd9d3;
  --sky-light:#92e1db;
  --teal:#12b3b8;
  --pink:#ec1b7d;
  --orange:#f36f21;
  --green:#7ab83a;
  --leaf:#2fa04a;
  --text:#555;
  --muted:#888;
  --white:#fff;
  --dash:#d9d9c9;
}
*{box-sizing:border-box;margin:0;padding:0}
html,body{width:738px;height:1200px;overflow:hidden}
body{
  position:relative;
  font-family:"Open Sans",sans-serif;
  color:var(--text);
  background:radial-gradient(ellipse at 50% 20%, var(--sky-light) 0%, var(--sky) 70%);
}
.abs{position:absolute}
.book-btn{left:106px;top:46px;width:130px;height:27px;background:var(--orange);color:var(--white);
  font-weight:700;font-size:11.5px;letter-spacing:.3px;display:flex;align-items:center;justify-content:center;border-radius:2px}
.brand{left:262px;top:40px;width:240px;height:40px;display:flex;align-items:center;justify-content:center;gap:6px;
  font-weight:700;font-size:16px;color:var(--leaf);white-space:nowrap}
.brand-dot{width:14px;height:14px;border-radius:50%;background:var(--orange);flex:none}
.social{top:50px;left:542px;display:flex;gap:6px}
.social span{width:18px;height:18px;border-radius:50%}
.s1{background:#3fb6e8}.s2{background:#3b5ea8}.s3{background:#555}.s4{background:#ea4c89}
.frame{left:106px;top:117px;width:527px;height:184px;background:var(--teal);border-radius:3px}
.nav{display:flex;height:33px}
.nav a{color:var(--white);text-decoration:none;font-weight:700;font-size:10px;display:flex;align-items:center;justify-content:center;position:relative;white-space:nowrap}
.nav .home{width:68px;background:var(--teal)}
.nav .attr{width:106px;background:var(--pink)}
.nav .attr::after{content:"";position:absolute;bottom:-6px;left:50%;margin-left:-6px;border:6px solid transparent;border-bottom:0;border-top-color:var(--pink)}
.nav .part{width:75px;background:var(--orange)}
.nav .pric{width:73px;background:var(--green)}
.nav .dire{width:93px;background:var(--pink)}
.nav .cont{width:112px;background:var(--teal)}
.hero{margin:4px 4px 0;height:143px;background:linear-gradient(180deg,#e8ded0,#c9b8a4 55%,#9a8a7e);border-bottom:3px solid var(--green)}
.card{background:var(--white);border-radius:3px;box-shadow:0 1px 3px rgba(0,0,0,.12)}
.card-inner{position:absolute;inset:6px;border:1px dashed var(--dash)}
.info{left:106px;top:314px;width:170px;height:202px}
.info-item{position:absolute;left:12px;right:12px;display:flex;gap:9px}
.info-icon{width:39px;height:39px;border-radius:50%;flex:none}
.info h3{font-size:9.5px;font-weight:600;margin-bottom:3px;white-space:nowrap}
.info p{font-size:6.5px;line-height:12.5px;color:var(--muted);text-align:justify}
.info .phone{font-size:9.5px;color:var(--green);white-space:nowrap}
.info-divider{position:absolute;left:7px;right:7px;top:79px;border-top:1px solid #eee}
.offers{left:106px;top:528px;width:170px;height:222px}
.offers-btn{position:absolute;left:18px;top:22px;width:134px;height:27px;background:var(--orange);color:var(--white);
  font-weight:700;font-size:14px;display:flex;align-items:center;justify-content:center;letter-spacing:.2px;white-space:nowrap}
.offers-photo{position:absolute;left:0;right:0;top:57px;bottom:0;background:linear-gradient(180deg,#f4ede4,#e8c8a0 55%,#e4463a 85%,#2f9e44);border-radius:0 0 3px 3px}
.main{left:288px;top:314px;width:345px;height:702px;border:2px solid var(--teal)}
.main .card-inner{inset:8px}
.illus{position:absolute;left:12px;top:18px;width:318px;height:176px;background:linear-gradient(180deg,#fff 0%,#f4efe6 40%,#e9a15a 60%,#6cc35a 100%)}
.content{position:absolute;left:23px;right:23px;top:204px}
.content h1{font-size:13px;font-weight:600;color:var(--leaf);padding-bottom:6px;border-bottom:1px solid #eee}
.intro{font-size:6.5px;line-height:12px;color:var(--muted);margin-top:8px}
.content h2{font-size:9.5px;font-weight:600;color:var(--leaf);margin-top:10px}
.price{font-size:7px;color:var(--text);margin-top:5px}
.list{list-style:none;margin-top:10px}
.list li{font-size:6.5px;color:var(--muted);height:15.8px;display:flex;align-items:center;gap:9px;white-space:nowrap}
.list li::before{content:"›";width:7px;height:7px;border-radius:50%;background:var(--orange);color:var(--white);font-size:7px;line-height:6px;text-align:center;font-weight:700;flex:none}
.footer{left:164px;top:1034px;width:409px;height:67px;border:1px dashed rgba(255,255,255,.7);border-radius:3px;text-align:center}
.footer-links{font-size:7.5px;color:#333;margin-top:9px;white-space:nowrap}
.footer-links span{margin:0 3px}
.address{font-size:10.5px;font-style:italic;color:var(--white);margin-top:6px;font-weight:600;white-space:nowrap}
.hours{font-size:8.5px;font-style:italic;color:var(--white);margin-top:6px;font-weight:600;white-space:nowrap}
.mountains{left:0;top:1104px;width:738px;height:96px;
  background:linear-gradient(180deg,rgba(255,255,255,0) 0%,#f4f7f7 28%,#dfe8e8 50%,#6fbf48 75%,#4ea83a 100%)}
</style>
</head>
<body>

<div class="abs book-btn">BOOK YOUR PARTY</div>

<div class="abs brand"><span class="brand-dot"></span>Meadow Moe's Funhouse</div>

<div class="abs social" aria-label="Social links">
  <span class="s1"></span><span class="s2"></span><span class="s3"></span><span class="s4"></span>
</div>

<div class="abs frame">
  <nav class="nav">
    <a class="home">HOME</a>
    <a class="attr">ATTRACTIONS</a>
    <a class="part">PARTIES</a>
    <a class="pric">PRICING</a>
    <a class="dire">DIRECTIONS</a>
    <a class="cont">CONTACT US</a>
  </nav>
  <div class="hero" role="img" aria-label="Photo of children playing with building blocks in a bright playroom"></div>
</div>

<aside class="abs card info">
  <div class="card-inner"></div>
  <div class="info-divider"></div>
  <div class="info-item" style="top:20px">
    <div class="info-icon" style="background:var(--orange)" role="img" aria-label="Toy blocks icon"></div>
    <div>
      <h3 style="color:var(--orange)">Party Invitations</h3>
      <p>Simply print and deliver to your party Guests.</p>
    </div>
  </div>
  <div class="info-item" style="top:96px">
    <div class="info-icon" style="background:var(--green)" role="img" aria-label="Book icon"></div>
    <div>
      <h3 style="color:var(--green)">How To Reserve</h3>
      <p><span class="phone">Call&nbsp;&nbsp; 555-014-2200</span><br>to reserve your party. A $25.00 deposit is required when booking a party. Deposit is refundable 48 hours prior to a party.</p>
    </div>
  </div>
</aside>

<aside class="abs card offers">
  <div class="card-inner"></div>
  <div class="offers-photo" role="img" aria-label="Photo of a smiling toddler building with colourful blocks"></div>
  <div class="offers-btn">ONLINE OFFERS</div>
</aside>

<main class="abs card main">
  <div class="card-inner"></div>
  <div class="illus" role="img" aria-label="Cartoon illustration of jungle animals and children around a birthday cake"></div>
  <div class="content">
    <h1>Birthday Party Packages :</h1>
    <p class="intro">Throw a wildly fun birthday party for your little jungle animals. We have 2 great birthday party packages to choose from:</p>

    <h2>Awesome Adventure</h2>
    <p class="price">$71.00 up to 5 children, $10.45 each additional child (plus tax)</p>
    <ul class="list">
      <li>Reserved Party table for two hours</li>
      <li>Unlimited rides and soft play pass for each child</li>
      <li>Balloon for each child</li>
      <li>Refillable dr</li>
      <li>inks for each child while at the table</li>
      <li>Slice of fresh baked pizza for each child</li>
      <li>Spin of party wheel for birthday child to win prizes</li>
      <li>5 game tokens for each child</li>
      <li>Free "Return Visit Pass" for the birthday child</li>
    </ul>

    <h2>The Ultimate</h2>
    <p class="price">$183.00 up to 10 children, $16.00 each additional child (plus tax)</p>
    <ul class="list">
      <li>Reserved Party table for two hours</li>
      <li>Unlimited rides and soft play pass for each child</li>
      <li>Balloon for each child</li>
      <li>Ice Cream for all children in the party</li>
      <li>Slice of fresh baked pizza for each child</li>
      <li>Spin of the party wheel for the birthday child to win prizes</li>
      <li>10 game tokens for each child</li>
      <li>Free "Return Visit Pass" for the birthday child</li>
      <li>A fun filled goody bag for each child</li>
      <li>Table cloth and colorful place settings</li>
      <li>Piñata for the children to break open at our piñata area</li>
      <li>Refillable drinks for each child while at the table</li>
    </ul>
  </div>
</main>

<footer class="abs footer">
  <div class="footer-links">Home Page<span>|</span>The Meadow Cafe<span>|</span>Attractions<span>|</span>Parties<span>|</span>Pricing<span>|</span>Group Outings<span>|</span>Directions<span>|</span>Contact Us</div>
  <div class="address">412 W. Clover Ridge Avenue in Maple Falls. Call 555-014-2200.</div>
  <div class="hours">Hours: Mon-Thu 11am-9pm, Fri 11am-10pm, Sat 10am-10pm</div>
</footer>

<div class="abs mountains" role="img" aria-label="Illustrated snowy mountain range with green hills"></div>

</body>
</html>
```